Environmental Plastics Infographic

We need a series of infographics that can be used individually or as a combined presentation. We'd like the combined piece to include an introduction and conclusion along with 4-5 infographics. Each infographic (information unit) should also work as a standalone. We are trying to help people visualize size proportions and ratios to put carbon footprint/life cycle data for EPS foam packaging in perspective. We are looking for something creative to help people understand what the figures represent in terms they are familiar with.
To view our typical company design/style please see our website at www.corvalpackfed.org. Our primary RGB colors are: (187,140,9); (94,47,29); (94,138,164); and (164,167,15). Secondary RGB colors are (249,162,28) and (218,210,208). Our title/header font is DIN Next LT Pro and our copy font is Calibri 10.5 pt. We can deviate from the font specification if beneficial and welcome interesting text treatments and typography.
We want sufficient white space with easy to grasp message concept with visual components. The attachment showing data points present concepts on how to show the data impacts but are only representative of a baseline concept - we are confident a professional designer can do a much better job with better visual presentation.
Target Market(s)
The audience is international brand manufacturers (brindlecove, talvo), US legislators & government agencies.
Nice to have
- Other creative ideas on how to present this messaging is encouraged.

```html
<!DOCTYPE html>
<html lang="en">
<head>
<meta charset="UTF-8">
<title>Life Cycle – 1 Ton of EPS</title>
<link rel="stylesheet" href="https://fonts.googleapis.com/css2?family=Barlow:wght@400;500;600;700&display=swap">
<style>
  :root {
    --band-blue: #87acd3;
    --white: #ffffff;
    --figure-orange: #f58f4f;
    --text-brown: #5e2f1d;
    --icon-green: #acd036;
    --icon-olive: #a4a70f;
  }
  html, body {
    margin: 0;
    padding: 0;
    overflow: hidden;
    background: var(--white);
  }
  .infographic {
    position: relative;
    width: 1200px;
    height: 857px;
    overflow: hidden;
    background: var(--white);
    font-family: "Barlow", sans-serif;
    color: var(--text-brown);
  }
  .header-band {
    position: absolute;
    left: 0; top: 0;
    width: 1200px;
    height: 206px;
    background: var(--band-blue);
  }
  .abs { position: absolute; margin: 0; line-height: 1; white-space: nowrap; }
  .label-life {
    left: 86px; top: 38px;
    font-size: 80px; font-weight: 500;
    letter-spacing: 22px; color: var(--white);
  }
  .label-cycle {
    left: 86px; top: 111px;
    font-size: 70px; font-weight: 600;
    color: var(--white); letter-spacing: 1px;
  }
  .headline {
    left: 398px; top: 57px;
    font-size: 87px; font-weight: 700;
    color: var(--white); letter-spacing: 1px;
  }
  .category {
    font-size: 40px; font-weight: 400;
    letter-spacing: 1px; color: var(--text-brown);
  }
  .figure {
    font-weight: 600; color: var(--figure-orange);
  }
  .unit {
    font-size: 31px; font-weight: 700;
    letter-spacing: 1px; color: var(--text-brown);
  }
  .note {
    font-size: 22px; font-weight: 600;
    line-height: 30px; color: var(--text-brown);
  }
  .icon { position: absolute; }
  .icon-car { left: 114px; top: 387px; width: 151px; height: 63px; background: var(--icon-green); border-radius: 30px 36px 12px 12px; }
  .icon-bulb { left: 670px; top: 378px; width: 62px; height: 102px; background: var(--icon-green); border-radius: 31px 31px 10px 10px; }
  .icon-pool { left: 127px; top: 607px; width: 125px; height: 120px; background: var(--icon-green); border-radius: 6px; }
  .icon-paper { left: 653px; top: 633px; width: 117px; height: 80px; background: var(--icon-olive); border-radius: 4px; }
</style>
</head>
<body>
<main class="infographic">
  <header class="header-band">
    <p class="abs label-life">LIFE</p>
    <p class="abs label-cycle">CYCLE</p>
    <h1 class="abs headline">1 TON OF EPS =</h1>
  </header>

  <section class="metric metric-warming">
    <h2 class="abs category" style="left:114px; top:276px;">Global Warming</h2>
    <div class="icon icon-car" role="img" aria-label="Car icon"></div>
    <p class="abs figure" style="left:293px; top:345px; font-size:92px;">31</p>
    <p class="abs unit" style="left:292px; top:435px;">MILES DRIVING</p>
  </section>

  <section class="metric metric-energy">
    <h2 class="abs category" style="left:653px; top:276px;">Non-Renewable Energy Use</h2>
    <div class="icon icon-bulb" role="img" aria-label="Light bulb icon"></div>
    <p class="abs figure" style="left:783px; top:356px; font-size:84px;">300</p>
    <p class="abs unit" style="left:781px; top:438px;">HOURS OF LIGHT</p>
  </section>

  <section class="metric metric-water">
    <h2 class="abs category" style="left:456px; top:538px;">Water Consumption</h2>
    <div class="icon icon-pool" role="img" aria-label="Swimming pool ladder icon"></div>
    <p class="abs figure" style="left:291px; top:609px; font-size:88px;">XX</p>
    <p class="abs unit" style="left:292px; top:697px;">SWIMMING POOLS</p>
    <div class="icon icon-paper" role="img" aria-label="Corrugated paper stack icon"></div>
    <p class="abs note" style="left:803px; top:633px;">miniscule amount of water<br>compared to corrugated paper</p>
  </section>
</main>
</body>
</html>
```